Landing page for selling a web application used by archeologists

We are selling a web program that professional archeologists use. This program is developed and designed already. But we are now building another website for presenting this web program.
I have uploaded a pdf file that shows the mockup of the future web page. You will also find a folder containing the photos used in the mockup. You can use your own photos for the ones named with "(can be changed)".
There is another folder called "otherPhoto". You can use them if you want to do background or ambiance...
We expect a really clean, serious, and professional design.

You will see in the mockup that there is a first part (main header) followed by 6 subparts presenting the different aspect of the web app. It finishes with the last part presenting ourselves and inviting to test the program.

Here are some links to website designs that go in the direction of what we want.
https://marovel.quintabrook.com/startup/#home
https://www.pathcrafter-wp. com/mobileapp-landing/
https://en.dravelpoint.com/
https://assets.korinthub.com/en/plyva-saas-software-landing-html5-page-template-RT4WN7/preview

Don't hesitate to contact me if you need more explanations.
As requested by a designer, I also added 2 print screen of the app that we are selling.
Updates

Feel free to use your own photos for background images for example...

Target Market(s)

Professional archaeologists

Industry/Entity Type

Archeology

Number of Pages Required

1 page

Colors
0054AA
0677BA
7BADD7
CADEEF
E8F1F8
0094D4
00A9DD
6FCCEA
C7EBF8
E9F6FB
FFC000
F8CF3A
FAE287
FDF2CF
FEFAEE

Requirements
Must have
• A professional look that says that our company is large and serious

```html
<!DOCTYPE html>
<html lang="en">
<head>
<meta charset="utf-8">
<title>StrataBase — Technology Serving Archeology</title>
<link href="https://fonts.googleapis.com/css2?family=Fredoka:wght@500;600&family=Poppins:wght@300;400;500;600&display=swap" rel="stylesheet">
<style>
:root{
  --blue:#58a9f3;
  --blue-deep:#3d8fe0;
  --blue-soft:#7badd7;
  --yellow:#fbc45a;
  --yellow-soft:#fae287;
  --ink:#2b2b2b;
  --text:#4a4a4a;
  --muted:#6b6b6b;
  --panel:#e9edf3;
  --band:#eceff3;
  --white:#ffffff;
}
*{box-sizing:border-box;margin:0;padding:0}
html,body{width:1200px;height:5209px;overflow:hidden}
body{position:relative;background:var(--white);font-family:"Poppins",sans-serif;color:var(--text)}
.abs{position:absolute}
.title{font-family:"Fredoka",sans-serif;font-weight:600;letter-spacing:2px;color:var(--ink)}
.btn{position:absolute;display:inline-block;background:var(--blue);color:var(--white);font-size:13px;border-radius:24px;padding:12px 16px;text-align:center;white-space:nowrap}
.lead{font-size:13.5px;line-height:24px}
.claim{font-size:16px;line-height:24px;color:var(--ink)}
.ph{position:absolute}

/* hero */
.brand{left:160px;top:22px;font-family:"Fredoka",sans-serif;font-weight:600;font-size:32px;letter-spacing:2px;color:var(--white);z-index:2}
.nav{left:455px;top:32px;display:flex;gap:44px;font-size:13px;color:var(--white);z-index:2}
.lang{left:855px;top:30px;display:flex;align-items:center;gap:8px;font-size:13px;color:var(--white);z-index:2}
.lang i{display:block;width:18px;height:13px;background:var(--white);border-radius:2px;opacity:.85}
.login{left:966px;top:20px;width:72px;height:40px;border-radius:20px;background:var(--blue-deep);color:var(--white);font-size:13px;line-height:40px;text-align:center;z-index:2}
.hero-h{left:162px;top:212px;font-family:"Fredoka",sans-serif;font-weight:600;font-size:34px;line-height:46px;letter-spacing:2px;color:var(--white);z-index:2;white-space:nowrap}
.hero-p{left:162px;top:314px;font-size:19px;line-height:30px;color:var(--white);width:300px;z-index:2}

/* feature blocks */
.feat-title{font-size:33px;white-space:nowrap}
.panel{left:162px;top:1238px;width:876px;height:486px;background:var(--panel);border-radius:36px}
.circle{position:absolute;width:234px;height:234px;border-radius:50%;border:5px solid var(--yellow)}
.circle.blue{border-color:var(--blue-soft)}
.view-box{left:573px;top:2559px;width:465px;height:364px;background:var(--blue);padding:44px 64px;color:var(--white)}
.view-box .title{color:var(--white);font-size:33px}
.about-band{left:0;top:3658px;width:1200px;height:621px;background:var(--band)}
.card{position:absolute;top:3941px;width:269px;height:449px;background:var(--white);border-radius:14px;box-shadow:0 10px 30px rgba(0,0,0,.07);padding:26px 24px;text-align:center}
.card h4{font-size:14px;font-weight:600;line-height:22px;color:var(--ink);margin-top:16px}
.card p{font-size:13px;line-height:24.5px;margin-top:28px}
.icon{width:86px;height:86px;margin:0 auto;display:block}

/* footer */
.footer{left:0;top:4937px;width:1200px;height:272px;background:var(--blue);border-radius:110px 110px 0 0;color:var(--white)}
.footer .brand2{position:absolute;left:0;width:1200px;top:64px;text-align:center;font-family:"Fredoka",sans-serif;font-weight:600;font-size:32px;letter-spacing:2px}
.footer .fnav{position:absolute;left:0;width:1200px;top:122px;display:flex;justify-content:center;gap:58px;font-size:13px}
.footer .copy{position:absolute;left:162px;top:196px;font-size:12px}
.footer .social{position:absolute;right:160px;top:196px;display:flex;gap:18px;font-size:12px;font-weight:500}
</style>
</head>
<body>

<!-- HERO -->
<svg class="abs" style="left:0;top:0" width="1200" height="540" viewBox="0 0 1200 540">
  <path d="M0 0H1200V536H110Q0 536 0 426Z" fill="var(--blue)"/>
  <polygon points="1020,0 1115,0 960,536 690,536" fill="var(--yellow)"/>
</svg>
<div class="abs brand">StrataBase</div>
<nav class="abs nav"><span>Solution</span><span>Price</span><span>Contact</span></nav>
<div class="abs lang"><i></i>English ⌄</div>
<div class="abs login">Login</div>
<h1 class="abs hero-h">Technology Serving<br>Archeology</h1>
<p class="abs hero-p">StrataBase The Solution To Input, Analyse And Promote The Archaeological Heritage</p>
<div class="ph" role="img" aria-label="Two desktop screens showing the StrataBase app: an excavation map and a data entry form" style="left:540px;top:132px;width:628px;height:478px;background:linear-gradient(160deg,#d9dde3,#8d9197);border-radius:18px;opacity:.95"></div>

<!-- ENTRY -->
<svg class="abs" style="left:0;top:630px" width="270" height="670" viewBox="0 0 270 670">
  <defs><linearGradient id="gy" x1="0" y1="0" x2="0" y2="1"><stop offset="0" stop-color="#f6c66a"/><stop offset="1" stop-color="#f0b843"/></linearGradient></defs>
  <polygon points="0,0 265,320 0,560" fill="var(--blue)"/>
  <polygon points="0,300 265,320 0,660" fill="url(#gy)"/>
  <polygon points="0,180 150,320 0,450" fill="var(--white)"/>
</svg>
<div class="ph" role="img" aria-label="Tablet showing the StrataEntry data capture form" style="left:192px;top:789px;width:466px;height:334px;background:linear-gradient(160deg,#3a3d42,#1c1e21);border-radius:22px"></div>
<div class="ph" style="left:214px;top:762px;width:80px;height:80px;border-radius:50%;background:var(--white);box-shadow:0 6px 18px rgba(0,0,0,.1)"></div>
<div class="ph" style="left:590px;top:890px;width:70px;height:70px;border-radius:50%;background:var(--white);box-shadow:0 6px 18px rgba(0,0,0,.1)"></div>
<div class="ph" style="left:290px;top:1060px;width:72px;height:72px;border-radius:50%;background:var(--white);box-shadow:0 6px 18px rgba(0,0,0,.1)"></div>
<h2 class="abs title feat-title" style="left:755px;top:842px">StrataEntry</h2>
<p class="abs lead" style="left:755px;top:896px;width:300px">Capture of archaeological information.<br>How to make more, faster, with the same amount of resources ?</p>
<p class="abs claim" style="left:755px;top:984px">StrataBase As Force Multiplier</p>
<span class="btn" style="left:755px;top:1036px;width:116px">More Details</span>

<!-- ANALYSIS -->
<div class="abs panel"></div>
<h2 class="abs title feat-title" style="left:0;width:1200px;text-align:center;top:1318px">StrataAnalysis</h2>
<p class="abs lead" style="left:0;width:1200px;text-align:center;top:1372px">Analysis of archaeological information<br>How to detect hidden relationships, make sense of the information and<br>preserve the big picture?</p>
<p class="abs claim" style="left:0;width:1200px;text-align:center;top:1462px">StrataBase as an intuitive solution&nbsp; to complex analysis problems.</p>
<span class="btn" style="left:541px;top:1510px;width:118px">More Details</span>
<div class="circle blue" style="left:223px;top:1584px;background:linear-gradient(160deg,#f4f6fa,#dfe4ec)" role="img" aria-label="Scatter plot with regression lines"></div>
<div class="circle" style="left:482px;top:1584px;background:linear-gradient(160deg,#ffffff,#eef0f4)" role="img" aria-label="Correspondence analysis chart"></div>
<div class="circle blue" style="left:741px;top:1584px;background:linear-gradient(160deg,#fde39b,#f29a3c)" role="img" aria-label="Heatmap with dendrogram"></div>

<!-- PUBLICATION -->
<h2 class="abs title feat-title" style="left:162px;top:2034px">StrataPublication</h2>
<p class="abs lead" style="left:162px;top:2086px;width:440px">Publication of archaeological information.<br>How to publish in a scientifc format and find the information scattered among multiple publications in Pdf format?</p>
<p class="abs claim" style="left:162px;top:2176px;width:320px">StrataBase as a tool for publishing and searching information</p>
<span class="btn" style="left:162px;top:2248px;width:118px">More Details</span>
<div class="ph" role="img" aria-label="Tablet displaying a published archaeological report" style="left:668px;top:1912px;width:368px;height:512px;background:linear-gradient(180deg,#7a5a47 0,#7a5a47 18%,#f3f3f3 18%,#e2e2e2 100%);border:14px solid #1f1f1f;border-radius:20px"></div>
<div class="ph" style="left:634px;top:2116px;width:78px;height:78px;border-radius:50%;background:var(--white);box-shadow:0 6px 18px rgba(0,0,0,.1)"></div>
<div class="ph" style="left:970px;top:2380px;width:70px;height:70px;border-radius:50%;background:var(--white);box-shadow:0 6px 18px rgba(0,0,0,.1)"></div>
<svg class="abs" style="left:1077px;top:1892px" width="123" height="600" viewBox="0 0 123 600">
  <polygon points="123,0 0,300 123,600" fill="var(--blue)"/>
  <polygon points="123,0 0,300 123,250" fill="#f3bf57"/>
  <polygon points="123,180 50,300 123,420" fill="var(--white)"/>
</svg>

<!-- VIEW -->
<div class="ph" role="img" aria-label="Photograph of a lakeside medieval castle" style="left:162px;top:2539px;width:486px;height:405px;background:linear-gradient(180deg,#c9d4e2 0,#b8a896 55%,#6f7d8d 100%);border-radius:0 0 60px 0"></div>
<div class="abs view-box">
  <h2 class="title">StrataView</h2>
  <p class="lead" style="margin-top:14px;font-size:13px">Promotion of the archaeological heritage.<br>How to render the archaeological heritage accessible to the general public, as well as to the educational and tourist sectors?</p>
  <p class="claim" style="color:var(--white);margin-top:14px;width:280px">StrataBase As A Mobilizing And Unifying Power</p>
  <span class="btn" style="position:static;display:inline-block;margin-top:22px;background:var(--white);color:var(--blue);width:118px">More Details</span>
</div>

<!-- FORUM / ARCHIVE -->
<div class="ph" role="img" aria-label="Illustration of a specialist at the centre of a global network of colleagues" style="left:216px;top:3035px;width:300px;height:262px;background:radial-gradient(circle at 50% 45%,#b9d6f5,#eef4fb 70%,#ffffff 71%)"></div>
<div class="ph" role="img" aria-label="Icons for XLS, PDF and DOC files" style="left:736px;top:3080px;width:200px;height:214px;background:linear-gradient(160deg,#e6f1fd,#fff3dc);border-radius:12px"></div>
<h2 class="abs title feat-title" style="left:166px;width:400px;text-align:center;top:3312px">StrataForum</h2>
<p class="abs lead" style="left:166px;width:400px;text-align:center;top:3364px">Staying in touch with the community.<br>How to connect among specialists and exchange ideas across borders and languages ?</p>
<p class="abs claim" style="left:166px;width:400px;text-align:center;top:3454px">StrataForum as a solution for<br>multilingual specialist networking</p>
<span class="btn" style="left:307px;top:3525px;width:118px">More Details</span>
<h2 class="abs title feat-title" style="left:632px;width:400px;text-align:center;top:3312px">StrataArchive</h2>
<p class="abs lead" style="left:632px;width:400px;text-align:center;top:3364px">Retrieval of information.<br>How to find information quickly within archives in various formats&nbsp; (pdf, xls, doc, etc.) ?</p>
<p class="abs claim" style="left:632px;width:400px;text-align:center;top:3454px">StrataBase As A Solution For<br>Dispersed Information</p>
<span class="btn" style="left:773px;top:3525px;width:118px">More Details</span>

<!-- ABOUT -->
<div class="abs about-band"></div>
<h2 class="abs title" style="left:0;width:1200px;text-align:center;top:3744px;font-size:33px">StrataBase</h2>
<p class="abs" style="left:0;width:1200px;text-align:center;top:3796px;font-family:'Fredoka',sans-serif;font-weight:600;font-size:23px;letter-spacing:1px;color:var(--blue)">Innovative, Reliable, At The Cutting Edge Of Technology</p>
<p class="abs lead" style="left:270px;width:660px;text-align:center;top:3848px">Founded by a Swiss team of computer engineers and statistical analysts, StrataBase places innovation at the service of success. Its vocation: to ofer the latest computer tools to the world of archaeology in order to facilitate and promote the work of archaeologists</p>

<div class="card" style="left:162px">
  <svg class="icon" viewBox="0 0 86 86"><circle cx="36" cy="28" r="15" fill="none" stroke="var(--blue)" stroke-width="3"/><path d="M10 76V64q0-14 26-14t26 14v12Z" fill="none" stroke="var(--blue)" stroke-width="3"/><circle cx="62" cy="66" r="11" fill="none" stroke="var(--yellow)" stroke-width="3"/></svg>
  <h4>The Expertise And Security<br>Of A Swiss Company</h4>
  <p>We bring together the most advanced technical engineering skills to deploy the right solutions for the most demanding problems. Big data input and processing, scalability, statistic analysis, deep learning, machine learning are our daily routine.</p>
</div>
<div class="card" style="left:465px">
  <svg class="icon" viewBox="0 0 86 86"><circle cx="30" cy="30" r="18" fill="none" stroke="var(--yellow)" stroke-width="3"/><path d="M52 20v44h-8l14 16 14-16h-8V20Z" fill="none" stroke="var(--blue)" stroke-width="3"/><path d="M24 50v20h-8l14 14" fill="none" stroke="var(--blue)" stroke-width="3"/></svg>
  <h4>Afordable<br>Prices</h4>
  <p>Budgets in archaeology are often limited. Reaching a large number of users allows advanced technological services that are usually very expensive to be ofered at very low prices.</p>
</div>
<div class="card" style="left:769px">
  <svg class="icon" viewBox="0 0 86 86"><rect x="12" y="22" width="62" height="40" fill="none" stroke="var(--blue)" stroke-width="3"/><rect x="26" y="8" width="34" height="20" rx="3" fill="none" stroke="var(--yellow)" stroke-width="3"/><path d="M43 62v16M28 80h30" stroke="var(--blue)" stroke-width="3"/></svg>
  <h4>Ongoing<br>Developments</h4>
  <p>Accompanied by professional archaeologists, we are continually shaping StrataBase to meet their precise needs and expectations. We are always listening to new development proposals in order to solve the problems that archeologists from all countries have in common.</p>
</div>

<!-- TRIAL -->
<svg class="abs" style="left:0;top:4372px" width="130" height="630" viewBox="0 0 130 630">
  <polygon points="0,0 125,330 0,630" fill="var(--blue)"/>
  <polygon points="0,0 125,330 0,300" fill="#f3bf57"/>
  <polygon points="0,180 70,330 0,460" fill="var(--white)"/>
</svg>
<div class="ph" role="img" aria-label="Laptop and tablet showing the StrataBase application" style="left:192px;top:4516px;width:486px;height:330px;background:linear-gradient(160deg,#3a3f47,#16181b);border-radius:14px"></div>
<h2 class="abs title" style="left:753px;top:4588px;font-size:30px;line-height:46px;white-space:nowrap">Get Now A<br>Free 3 Month Trial<br>Of StrataBase</h2>
<span class="btn" style="left:753px;top:4740px;width:118px">Contact Us</span>

<!-- FOOTER -->
<footer class="abs footer">
  <div class="brand2">StrataBase</div>
  <nav class="fnav"><span>Home</span><span>Solution</span><span>Price</span><span>Contact</span></nav>
  <div class="copy">© 2022 StrataBase. All Rights Reserved.</div>
  <div class="social"><span>Faceline</span><span>Chirper</span><span>Linkwork</span><span>Circlo</span></div>
</footer>

</body>
</html>
```